Presentation Folder for Crest Holdings

We are a new property management / real estate company in Denver Colorado and are in need of new stationary design. Attached are our business card and logo deigns. We are looking for our stationary design. We need a presentation folder design that is Professional, exciting, and approachable. We do not have a preference on folder layout (pockets, style of folding) but will most likely be using a standard two pocket folder design (roughly 9x12) but feel free to experiment with and folder style as long as we can find a place to print them. We would also like to have a matching letterhead/page design
Below is standard size of folder from plume press
Full Bleed Size
20.87" x 16.68"
53 x 42.4 cm
6260 x 5004 pixels
Document Trim Size
20.75" x 16.56"
52.7 x 42.1 cm
6225 x 4969 pixels
Target Market(s)
We are attempting to target the top end of the real estate market in Denver Colorado. Are target market is investors in real estate.
Industry/Entity Type
Property Management
Font styles to use
Other font styles liked:
- Would like to keep font same to logo
Look and feel
Each slider illustrates characteristics of the customer's brand and the style your logo design should communicate.

```html
<!DOCTYPE html>
<html lang="en">
<head>
<meta charset="utf-8">
<title>Crest Holdings – Letterhead and Presentation Folder</title>
<link rel="stylesheet" href="https://fonts.googleapis.com/css2?family=Oswald:wght@300;500&family=Crimson+Text:ital@1&display=swap">
<style>
  :root {
    --backdrop: #e9eaec;
    --paper: #ffffff;
    --ink: #2f2f33;
    --ink-soft: #6d6e72;
    --brand-blue: #3d9fd4;
    --folder: #2a2929;
    --folder-edge: #1f1e1e;
    --rule: #cfd2d6;
  }
  * { box-sizing: border-box; margin: 0; padding: 0; }
  html, body { width: 1200px; height: 695px; overflow: hidden; }
  body {
    background: var(--backdrop);
    position: relative;
    font-family: "Crimson Text", Georgia, serif;
    color: var(--ink);
  }

  /* Letterhead */
  .letterhead {
    position: absolute;
    left: 80px; top: 30px;
    width: 490px; height: 635px;
    background: var(--paper);
    box-shadow: 0 4px 14px rgba(0,0,0,.12);
  }
  .letterhead__brand {
    position: absolute; left: 48px; top: 38px;
    display: flex; align-items: center; gap: 10px;
  }
  .brand-dot {
    width: 26px; height: 26px; border-radius: 50%;
    border: 3px solid var(--brand-blue);
  }
  .brand-name {
    font-family: "Oswald", sans-serif; font-weight: 500;
    font-size: 24px; letter-spacing: .5px; text-transform: uppercase;
    color: var(--brand-blue);
  }
  .letterhead__rule {
    position: absolute; left: 250px; right: 48px; top: 118px;
    border-top: 1px solid var(--rule);
  }
  .letter {
    position: absolute; left: 48px; right: 48px; top: 92px;
    font-style: italic; font-size: 11.5px; line-height: 1.35;
  }
  .letter p { margin-bottom: 12px; }
  .letter address { font-style: italic; margin-bottom: 12px; }
  .signature {
    position: absolute; right: 60px; bottom: 60px;
    width: 70px; height: 44px;
    background: #f3f4f6;
  }
  .letterhead__footer {
    position: absolute; left: 48px; right: 48px; bottom: 24px;
    font-family: "Oswald", sans-serif; font-weight: 300;
    font-size: 8.5px; letter-spacing: .3px; color: var(--ink-soft);
  }
  .letterhead__band {
    position: absolute; left: 0; right: 0; bottom: 0; height: 9px;
    background: var(--brand-blue);
  }

  /* Presentation folder cover */
  .folder {
    position: absolute;
    left: 640px; top: 30px;
    width: 480px; height: 635px;
    background: radial-gradient(circle at 50% 40%, #333232, var(--folder) 70%, var(--folder-edge));
    box-shadow: 0 4px 14px rgba(0,0,0,.25);
    display: flex; align-items: center; justify-content: center;
  }
  .folder__brand { display: flex; align-items: center; gap: 14px; margin-top: -40px; }
  .folder__brand .brand-dot { width: 40px; height: 40px; border-width: 4px; }
  .folder__brand .brand-name { font-size: 34px; }
</style>
</head>
<body>

<section class="letterhead" aria-label="Crest Holdings letterhead">
  <div class="letterhead__brand">
    <span class="brand-dot"></span>
    <span class="brand-name">Crest Holdings</span>
  </div>
  <div class="letterhead__rule"></div>

  <div class="letter">
    <address>4120 Aspen Ridge Street<br>Denver, CO 80202</address>
    <p>January 29th, 2017</p>
    <address>Ms. Harlow<br>President, Harlow Family Center<br>318 Meadow Lane<br>Boulder, CO 80302</address>
    <p>Dear Ms. Harlow:</p>
    <p>In the first paragraph, one needs to give a brief introduction of oneself. One should also give reference to the purpose of the letter in brief. The second paragraph needs to give the details of the letter and its need. This paragraph is usually longer than the others and plays the main role in the letter. Keep the sentences short and to the point. Avoid using complex words and sentences.</p>
    <p>The third and last paragraph is the conclusion of the letter and can be kept short.</p>
    <p>Sincerely,</p>
    <p>(This is where the signature of the writer will be placed)</p>
    <p>Dana Whitfield<br>Read more at: www.letterguide.net/articles/professional-letter-format-example.html</p>
  </div>

  <div class="signature" role="img" aria-label="Handwritten signature of the writer"></div>

  <p class="letterhead__footer">Crest Holdings · 4120 Aspen Ridge Street · Denver, CO 80202 · Phone 303 555 0148 · hello@crestholdings.com</p>
  <div class="letterhead__band"></div>
</section>

<section class="folder" aria-label="Crest Holdings presentation folder cover">
  <div class="folder__brand">
    <span class="brand-dot"></span>
    <span class="brand-name">Crest Holdings</span>
  </div>
</section>

</body>
</html>
```